Valto Sàrl - Business Card

VALTO Sàrl operates in the sector Services for banks and credit institutions. It is a B2B which connects companies. The main colors should be Blue and Black. The logo and look of the card should be simple, professional, conservative and reflect Connecting People.

Target Market(s)

Financial professionals and institutions

Industry/Entity Type

Finance

Contact Information for Business Card

Chemin des Prés 9
1027 Lonay

Logo Text

Halden Partners

Font styles to use
Serif
Sans Serif

Colors
0355a3
3176b5
85acd3
cfdeed

Requirements
Should not have
• Multiple colors

```html
<!DOCTYPE html>
<html lang="en">
<head>
<meta charset="utf-8">
<title>Valto Sàrl – Business Card</title>
<link rel="stylesheet" href="https://fonts.googleapis.com/css2?family=Open+Sans:wght@400;600&display=swap">
<style>
  :root {
    --blue-deep: #0355a3;
    --blue-mid: #3176b5;
    --blue-light: #85acd3;
    --blue-pale: #cfdeed;
    --ink: #111111;
    --paper: #f2f2f2;
    --backdrop: #e4e7eb;
  }
  * { box-sizing: border-box; margin: 0; padding: 0; }
  html, body { width: 1200px; height: 800px; overflow: hidden; }
  body {
    background: var(--backdrop);
    font-family: "Open Sans", Arial, sans-serif;
    display: flex;
    align-items: center;
    justify-content: center;
    gap: 60px;
  }
  .card {
    width: 520px;
    height: 297px;
    position: relative;
    box-shadow: 0 10px 28px rgba(0, 0, 0, 0.18);
  }

  /* Front: blue face with brand name */
  .card--front {
    background: var(--blue-deep);
    display: flex;
    flex-direction: column;
    align-items: center;
    justify-content: center;
    gap: 8px;
  }
  .brand__name {
    font-size: 32px;
    font-weight: 600;
    color: var(--ink);
    letter-spacing: 0.5px;
    white-space: nowrap;
  }
  .front__web {
    font-size: 11px;
    color: var(--ink);
    letter-spacing: 0.3px;
    align-self: flex-end;
    margin-right: 122px;
  }

  /* Back: white face with contact details */
  .card--back {
    background: var(--paper);
    display: grid;
    grid-template-columns: 190px 1fr;
    align-items: center;
    padding: 0 30px;
  }
  .back__brand .brand__name {
    font-size: 19px;
    font-weight: 600;
    color: var(--blue-mid);
  }
  .back__details {
    border-left: 1.5px solid var(--ink);
    padding-left: 26px;
    height: 190px;
    display: flex;
    flex-direction: column;
    justify-content: center;
  }
  .person__name {
    font-size: 22px;
    font-weight: 600;
    color: var(--blue-deep);
    line-height: 1;
  }
  .person__role {
    font-size: 13px;
    color: var(--ink);
    margin-bottom: 16px;
    letter-spacing: 0.3px;
  }
  .contact {
    list-style: none;
    font-size: 12.5px;
    color: var(--ink);
    display: flex;
    flex-direction: column;
    gap: 6px;
  }
  .contact__item {
    display: flex;
    align-items: flex-start;
    gap: 10px;
    line-height: 1.3;
    white-space: nowrap;
  }
  .contact__icon {
    width: 14px; height: 14px;
    flex: none;
    margin-top: 1px;
  }
</style>
</head>
<body>

  <section class="card card--front" aria-label="Business card front">
    <p class="brand__name">Halden Partners</p>
    <p class="front__web">www.haldenpartners.ch</p>
  </section>

  <section class="card card--back" aria-label="Business card back">
    <div class="back__brand">
      <p class="brand__name">Halden Partners</p>
    </div>
    <div class="back__details">
      <p class="person__name">NAME HERE</p>
      <p class="person__role">DESIGNATION</p>
      <ul class="contact">
        <li class="contact__item">
          <svg class="contact__icon" viewBox="0 0 16 16" aria-hidden="true"><path d="M4 1.5 6.2 4.3 5 6c.8 1.9 2.6 3.8 5 5l1.7-1.2L14.5 12l-1.6 2.4C7 14 2 9 1.6 3.1Z" fill="#111"/></svg>
          <span>021 555 01 23</span>
        </li>
        <li class="contact__item">
          <svg class="contact__icon" viewBox="0 0 16 16" aria-hidden="true"><rect x="1.5" y="3.5" width="13" height="9" fill="none" stroke="#111" stroke-width="1.2"/><path d="M1.5 3.5 8 9l6.5-5.5" fill="none" stroke="#111" stroke-width="1.2"/></svg>
          <span>contact@haldenpartners.ch</span>
        </li>
        <li class="contact__item">
          <svg class="contact__icon" viewBox="0 0 16 16" aria-hidden="true"><circle cx="8" cy="8" r="6.5" fill="none" stroke="#111" stroke-width="1.2"/><ellipse cx="8" cy="8" rx="3" ry="6.5" fill="none" stroke="#111" stroke-width="1"/><path d="M1.5 8h13" stroke="#111" stroke-width="1"/></svg>
          <span>www.haldenpartners.ch</span>
        </li>
        <li class="contact__item">
          <svg class="contact__icon" viewBox="0 0 16 16" aria-hidden="true"><path d="M8 15S3 9.5 3 6a5 5 0 0 1 10 0c0 3.5-5 9-5 9Z" fill="#111"/><circle cx="8" cy="6" r="1.8" fill="#f2f2f2"/></svg>
          <span>Address Line 1 Here,<br>Address Line 2 Here</span>
        </li>
      </ul>
    </div>
  </section>

</body>
</html>
```